New York City Sponsorship Page with Click Through Supporting Pages

Metro Talent Guild, the leading New York City resource for HR Professionals is a membership organization with almost 2,000 individual members.

We need section/page(s) created for our current sponsorship offerings. Our platform is on ClubNest Suite Platform and we need capability to edit the page, etc. It must be HTML ready/coded.

Attached is the mock up of how we want the page to look (pages mockup pdf) as well as each of the categories which should be included (in the excel files). Our current page is here: http://www.metrotalentguild.example/?page=sponsors and is not easy to read through. We want something that is visually appealing and clean but showcases all of the different ways to sponsor the Chapter.

Additionally, we are taking the information from this page and turning it into a brochure.

Target Market(s)

New York City Companies who have HR Professionals or services they want to attract or offer.

Coding

Coded - Design and coding required

Number of Pages Required

5+ page

Requirements
Must have
• Clean Look and feel, easy functionality, necessary information and purchases. Match the top navigation of current page. Opportunity for current sponsor logos to be highlighted on the page. Easy to update/maintain.
Nice to have
• Option to pay for sponsorships through the page using our credit card processor.
Should not have
• Overwhelming text in sections

```html
<!DOCTYPE html>
<html lang="en">
<head>
<meta charset="utf-8">
<title>Invitation for Sponsors – Metro Talent Guild</title>
<link href="https://fonts.googleapis.com/css2?family=Open+Sans:wght@400;600;700&family=Rubik:wght@500;700&family=Roboto+Condensed:wght@400&display=swap" rel="stylesheet">
<style>
:root{
  --navy:#0d2a44;
  --navy-deep:#0a2238;
  --teal-navy:#124469;
  --blue:#1583d0;
  --red:#c00d12;
  --charcoal:#2c2f33;
  --ink:#1a1a1a;
  --link:#1b74b9;
  --grey-bg:#ececec;
  --section-grey:#eeeeee;
  --rule:#c9c9c9;
  --white:#ffffff;
}
*{margin:0;padding:0;box-sizing:border-box}
html,body{width:843px;height:1200px;overflow:hidden}
body{background:var(--grey-bg);font-family:"Open Sans",sans-serif;color:var(--ink);position:relative}
.page{position:absolute;left:10px;top:10px;width:823px;height:1180px;background:var(--white);overflow:hidden}

/* top utility bar */
.utility{height:21px;background:var(--navy);position:relative}
.utility-links{position:absolute;left:432px;top:6px;display:flex;gap:9px;font-size:7px;font-weight:700;color:var(--white);letter-spacing:.1px}
.search{position:absolute;left:574px;top:4px;width:98px;height:13px;background:var(--white);font-size:6px;color:#999;padding:3px 4px}
.social-top{position:absolute;left:678px;top:4px;display:flex;gap:5px}
.social-top span{width:14px;height:14px;background:#1e88d1;display:block}

/* header */
.header{height:54px;position:relative;background:#f7f7f7}
.brand{position:absolute;left:60px;top:16px;display:flex;align-items:center;gap:6px;font-family:"Rubik",sans-serif;font-weight:700;font-size:14px;color:var(--red)}
.brand i{width:14px;height:14px;border-radius:50%;background:var(--navy);display:block}
.nav{position:absolute;left:267px;top:21px;display:flex;gap:21px;font-family:"Roboto Condensed",sans-serif;font-size:11.5px;color:var(--link)}

.hero{height:94px;background:linear-gradient(180deg,#25303c 0%,#161b22 55%,#0b0e12 100%)}

.crumbs{height:26px;position:relative;font-size:7px;font-weight:600;color:#222}
.crumbs .path{position:absolute;left:24px;top:9px}
.crumbs .share{position:absolute;left:760px;top:8px;display:flex;align-items:center;gap:4px}

/* section titles */
.title{position:absolute;left:0;width:823px;display:flex;align-items:center;justify-content:center;gap:14px;font-family:"Rubik",sans-serif;font-weight:500}
.title .line{height:1px;background:var(--rule)}
.title em{font-style:normal;color:var(--red)}

.invite{height:170px;position:relative}
.invite .title{top:46px;font-size:17px;color:var(--navy);font-weight:700}
.invite p{position:absolute;left:0;width:823px;text-align:center;font-size:8.4px;font-weight:600;color:#222}

/* categories */
.categories{height:292px;background:var(--section-grey);position:relative}
.categories .title{top:40px;font-size:14px;color:var(--navy)}
.card{position:absolute;top:110px;width:178px;height:128px;color:var(--white);text-align:center}
.card h3{position:absolute;left:52px;top:10px;width:116px;font-family:"Rubik",sans-serif;font-weight:500;font-size:11.5px;line-height:13px}
.card p{position:absolute;left:16px;top:50px;width:146px;font-size:8.6px;line-height:12px}
.card .badge{position:absolute;left:-12px;top:-19px;width:56px;height:56px;border-radius:50%;border:3px solid var(--white);display:flex;align-items:center;justify-content:center}
.card .price{position:absolute;left:37px;top:116px;width:104px;height:28px;border-radius:3px;border:1.5px solid var(--white);font-family:"Rubik",sans-serif;font-weight:500;font-size:14px;line-height:25px}
.c1{left:66px;background:var(--teal-navy);border-radius:4px 0 0 4px;box-shadow:0 0 0 3px var(--white)}
.c2{left:244px;background:var(--blue)}
.c3{left:422px;background:var(--red)}
.c4{left:600px;background:var(--charcoal);border-radius:0 4px 4px 0}
.c1 .badge,.c1 .price{background:var(--teal-navy)}
.c2 .badge,.c2 .price{background:var(--blue)}
.c3 .badge,.c3 .price{background:var(--red)}
.c4 .badge,.c4 .price{background:var(--charcoal)}

/* actions band */
.actions{height:142px;position:relative;background:linear-gradient(180deg,#3d5670 0%,#2c4660 50%,#1f3650 100%)}
.action{position:absolute;top:53px;width:204px;height:36px;background:var(--white);border-radius:3px;font-family:"Rubik",sans-serif;font-weight:500;font-size:10.5px;line-height:12.5px;color:#111;text-align:center;padding:6px 0 0 60px}
.action .ring{position:absolute;left:-4px;top:-15px;width:64px;height:64px;border-radius:50%;background:var(--white);border:2px solid #d5d5d5;display:flex;align-items:center;justify-content:center}
.a1{left:100px}.a2{left:324px}.a3{left:548px}

/* sponsors */
.sponsors{height:202px;position:relative}
.sponsors .title{top:40px;font-size:13.5px;color:var(--navy)}
.tier{position:absolute;top:92px;font-family:"Rubik",sans-serif;font-weight:500;font-size:13px;color:#333}
.sponsor{position:absolute;top:124px;font-family:"Open Sans",sans-serif;font-weight:700;font-size:18px;color:var(--teal-navy);display:flex;align-items:center;gap:6px}
.sponsor i{width:10px;height:10px;background:var(--teal-navy);display:block}

/* footer */
.footer{height:156px;background:var(--navy);position:relative;color:var(--white)}
.footer h4{position:absolute;top:21px;font-family:"Roboto Condensed",sans-serif;font-weight:400;font-size:14px}
.footer ul{list-style:none;position:absolute;top:46px;font-size:7.8px;line-height:14.5px}
.footer .contact{position:absolute;left:209px;top:46px;font-size:7.8px;line-height:21px}
.affiliate{position:absolute;left:353px;top:23px;width:143px;height:104px;background:var(--white);display:flex;align-items:center;justify-content:center}
.affiliate span{width:110px;height:70px;background:#5577a8;display:block}
.social-foot{position:absolute;left:553px;top:48px;display:flex;gap:6px}
.social-foot span{width:23px;height:23px;background:#1e88d1;display:block}
.legal{height:38px;background:var(--navy-deep);color:var(--white);font-size:6.8px;font-weight:600;text-align:center;line-height:38px}
</style>
</head>
<body>
<div class="page">
  <div class="utility">
    <div class="utility-links"><span>CONTACT US</span><span>SIGN IN</span><span>JOIN/RENEW</span></div>
    <div class="search">Enter search criteria...</div>
    <div class="social-top"><span></span><span></span><span></span><span></span><span></span></div>
  </div>

  <header class="header">
    <div class="brand"><i></i>Metro Talent Guild</div>
    <nav class="nav"><span>Our New Website</span><span>About Us</span><span>Membership</span><span>Events</span><span>Sponsorships</span><span>Career Center</span><span>HR Resources</span></nav>
  </header>

  <div class="hero" role="img" aria-label="Night skyline of Manhattan with lit skyscrapers"></div>

  <div class="crumbs">
    <span class="path">SPONSORSHIPS &gt; SPONSORSHIP OPPORTUNITIES</span>
    <span class="share">SHARE
      <svg width="12" height="12" viewBox="0 0 12 12"><circle cx="9.5" cy="2.5" r="2" fill="#111"/><circle cx="2.5" cy="6" r="2" fill="#111"/><circle cx="9.5" cy="9.5" r="2" fill="#111"/><path d="M2.5 6 9.5 2.5M2.5 6 9.5 9.5" stroke="#111" stroke-width="1.3"/></svg>
    </span>
  </div>

  <section class="invite">
    <div class="title"><span class="line" style="width:130px"></span><span>INVITATION FOR <em>SPONSORS</em></span><span class="line" style="width:125px"></span></div>
    <p style="top:100px">Thank you for your interest in Metro Talent Guild.</p>
    <p style="top:128px">As a premier HR chapter, we offer many opportunities to increase your exposure to the New York City HR community.</p>
  </section>

  <section class="categories">
    <div class="title"><span class="line" style="width:65px"></span><span>Choose the sponsorship category <em>that best meets your needs:</em></span><span class="line" style="width:65px"></span></div>

    <div class="card c1">
      <div class="badge"><svg width="32" height="28" viewBox="0 0 32 28" fill="#fff"><circle cx="9" cy="5" r="3.5"/><circle cx="23" cy="5" r="3.5"/><path d="M4 11h10v8h-2v9H7v-9H4zM18 11h10v8h-3v9h-5v-9h-2z"/></svg></div>
      <h3>Strategic Partnership</h3>
      <p>Opportunities for a strategic sponsorship at different levels, each providing a valuable set of great benefits.</p>
      <div class="price">$3,500+</div>
    </div>
    <div class="card c2">
      <div class="badge"><svg width="32" height="26" viewBox="0 0 32 26" fill="#fff"><circle cx="8" cy="7" r="3"/><circle cx="16" cy="5" r="3"/><circle cx="24" cy="7" r="3"/><path d="M2 22l5-10h18l5 10z"/></svg></div>
      <h3>Programs / Events</h3>
      <p>Opportunities to sponsor a wide range of events like all-day conference, 2 hour sessions etc.</p>
      <div class="price">$500+</div>
    </div>
    <div class="card c3">
      <div class="badge"><svg width="32" height="28" viewBox="0 0 32 28" fill="none" stroke="#fff" stroke-width="2.2"><path d="M4 10h6l12-7v20L10 16H4z"/><path d="M8 16l2 8h4"/><path d="M26 7l4-2M26 13h5M26 19l4 2"/></svg></div>
      <h3>Advertising / Promotion</h3>
      <p>Opportunities for regular or one time digital sponsoring in form of website banners, website ads, e-blasts etc.</p>
      <div class="price">$150+</div>
    </div>
    <div class="card c4">
      <div class="badge"><svg width="30" height="28" viewBox="0 0 30 28" fill="#fff"><rect x="2" y="8" width="12" height="7"/><rect x="2" y="18" width="26" height="7"/><path d="M22 2l5 6h-3v7h-4V8h-3z"/></svg></div>
      <h3>Custom</h3>
      <p>Build your own sponsorship program from our variety of opportunities.</p>
      <div class="price">$250+</div>
    </div>
  </section>

  <section class="actions" role="img" aria-label="Muted blue aerial view of the New York City skyline">
    <div class="action a1"><div class="ring"><svg width="36" height="30" viewBox="0 0 36 30" fill="none" stroke="#0d2a44" stroke-width="2"><rect x="2" y="4" width="28" height="20" rx="2"/><path d="M2 6l14 10L30 6"/><path d="M24 20l8-4v10l-8-4z" fill="#1583d0" stroke="#1583d0"/></svg></div>More about our<br>sponsorship packages</div>
    <div class="action a2"><div class="ring"><svg width="36" height="36" viewBox="0 0 36 36" fill="none" stroke-width="3"><circle cx="16" cy="20" r="13" stroke="#1583d0"/><circle cx="16" cy="20" r="7" stroke="#1583d0"/><circle cx="16" cy="20" r="2" fill="#1583d0" stroke="none"/><path d="M16 20L31 5" stroke="#0d2a44"/></svg></div>Book your<br>sponsorship packages</div>
    <div class="action a3"><div class="ring"><svg width="34" height="34" viewBox="0 0 34 34" fill="none" stroke="#c00d12" stroke-width="2.2"><path d="M8 4l5 7-3 3c2 4 6 8 10 10l3-3 7 5-3 5C15 30 4 19 3 7z"/><path d="M20 9a6 6 0 0 1 5 5M20 4a11 11 0 0 1 10 10"/></svg></div>Contact our<br>sponsorship team</div>
  </section>

  <section class="sponsors">
    <div class="title"><span class="line" style="width:65px"></span><span>Thanks to <em>our sponsors</em></span><span class="line" style="width:65px"></span></div>
    <div class="tier" style="left:83px">Gold</div>
    <div class="tier" style="left:433px">Silver</div>
    <div class="sponsor" style="left:83px">Harlow &amp; Pike</div>
    <div class="sponsor" style="left:238px">Transit Perks Co.</div>
    <div class="sponsor" style="left:433px"><i></i>Bastion Benefits</div>
    <div class="sponsor" style="left:612px">Staffwell</div>
  </section>

  <footer class="footer">
    <h4 style="left:83px">Navigation</h4>
    <ul style="left:83px"><li>About Us</li><li>Membership</li><li>Events</li><li>Career Center</li><li>Sponsorships</li><li>HR Resources</li></ul>
    <h4 style="left:209px">Contact Us</h4>
    <div class="contact">Phone: 555-010-4769<br>Fax: 555-010-8244<br>info@metrotalentguild.example</div>
    <div class="affiliate" role="img" aria-label="Affiliate badge"><span></span></div>
    <h4 style="left:553px">Connect With Us</h4>
    <div class="social-foot"><span></span><span></span><span></span><span></span><span></span></div>
  </footer>
  <div class="legal">Membership Software Powered by ClubNest Suite &nbsp;::&nbsp; Legal</div>
</div>
</body>
</html>
```